Brightkeel Logistics - Cards and Logo

We need a logo and card design for a Logistics company located in Chicago. Our competitors are KTR and Qorvan. We would like to see designs that incorporate a logo that shows all ways in terms of direction. The colors would be Electric Blue, Grays, Blacks and White. I like how Moko has a badge type logo that is strong and clean. Velmora also has a strong font that is futuristic. The final design should communicate we are a strong and technological type of company. I show a picture of the colors we like from a moko cooler.

```html
<!DOCTYPE html>
<html lang="en">
<head>
<meta charset="utf-8">
<title>Brightkeel Logistics – Business Card</title>
<link href="https://fonts.googleapis.com/css2?family=Quicksand:wght@400;500;700&display=swap" rel="stylesheet">
<style>
  :root {
    --page: #ffffff;
    --navy-blue: #156f98;
    --electric-blue: #2a9ad8;
    --steel-gray: #c3c8cb;
    --card-gray: #bbbfc2;
    --glow: #f4f5f6;
    --icon-teal: #4cc3c4;
    --white: #ffffff;
    --edge: #9fb3bd;
  }
  * { margin: 0; padding: 0; box-sizing: border-box; }
  html, body { width: 1200px; height: 1200px; overflow: hidden; background: var(--page); }
  body { position: relative; font-family: "Quicksand", sans-serif; }

  .card { position: absolute; left: 198px; width: 803px; border: 1px solid var(--edge); overflow: hidden; }
  .card-front { top: 112px; height: 493px; background: var(--white); }
  .card-back {
    top: 606px; height: 481px;
    background: radial-gradient(ellipse 300px 190px at 50% 50%, var(--glow) 0%, var(--glow) 35%, var(--card-gray) 100%);
  }

  .card-art { position: absolute; inset: 0; width: 100%; height: 100%; }

  .company-title {
    position: absolute; left: 48px; top: 100px;
    color: var(--white); font-weight: 700; font-size: 29px; letter-spacing: -0.3px;
  }

  .contact-list { position: absolute; left: 48px; top: 196px; list-style: none; }
  .contact-item { display: flex; align-items: center; height: 40px; margin-bottom: 22px; }
  .contact-item svg { width: 40px; height: 40px; flex: none; }
  .contact-text { margin-left: 14px; color: var(--white); font-size: 18px; font-weight: 500; }

  .brand-name {
    position: absolute; color: var(--electric-blue); font-weight: 700; white-space: nowrap;
    transform: translateX(-50%);
  }
  .card-front .brand-name { left: 606px; top: 262px; font-size: 33px; }
  .card-back .brand-name { left: 50%; top: 218px; font-size: 40px; }
</style>
</head>
<body>

<section class="card card-front">
  <svg class="card-art" viewBox="0 0 803 493" aria-hidden="true">
    <path fill="var(--navy-blue)" d="M0 0 H238 C300 50 330 160 370 260 C410 360 440 440 488 493 H0 Z"/>
    <path fill="var(--steel-gray)" d="M598 48 L690 22 C740 60 780 130 803 176 V208 C760 150 690 80 598 48 Z"/>
    <path fill="var(--electric-blue)" d="M690 24 L734 0 H803 V132 C770 90 730 50 690 24 Z"/>
  </svg>

  <h1 class="company-title">Brightkeel Logistics</h1>

  <ul class="contact-list">
    <li class="contact-item">
      <svg viewBox="0 0 40 40" aria-hidden="true"><circle cx="20" cy="20" r="18" fill="none" stroke="var(--icon-teal)" stroke-width="2.5"/><path fill="var(--icon-teal)" d="M14 12 l3 -1 l2 5 l-2 1.5 c1 2.5 2.5 4 5 5 l1.5 -2 l5 2 l-1 3 c-8 1 -14 -5 -13.5 -13.5z"/></svg>
      <span class="contact-text">+000 12345 6789</span>
    </li>
    <li class="contact-item">
      <svg viewBox="0 0 40 40" aria-hidden="true"><circle cx="20" cy="20" r="18" fill="none" stroke="var(--icon-teal)" stroke-width="2.5"/><path fill="var(--icon-teal)" d="M27 13 L13 19 L19 21 L21 27 Z"/></svg>
      <span class="contact-text">urname@email.com</span>
    </li>
    <li class="contact-item">
      <svg viewBox="0 0 40 40" aria-hidden="true"><circle cx="20" cy="20" r="18" fill="none" stroke="var(--icon-teal)" stroke-width="2.5"/><path fill="none" stroke="var(--icon-teal)" stroke-width="2.2" d="M20 28 C15 22 14.5 19.5 14.5 17.5 A5.5 5.5 0 0 1 25.5 17.5 C25.5 19.5 25 22 20 28 Z"/><circle cx="20" cy="17.5" r="1.8" fill="var(--icon-teal)"/></svg>
      <span class="contact-text">Street Address Here</span>
    </li>
    <li class="contact-item">
      <svg viewBox="0 0 40 40" aria-hidden="true"><circle cx="20" cy="20" r="18" fill="none" stroke="var(--icon-teal)" stroke-width="2.5"/><g fill="var(--icon-teal)" stroke="var(--icon-teal)" stroke-width="1.8"><line x1="15" y1="20" x2="24" y2="15"/><line x1="15" y1="20" x2="24" y2="25"/><circle cx="15" cy="20" r="2.6"/><circle cx="24.5" cy="14.5" r="2.6"/><circle cx="24.5" cy="25.5" r="2.6"/></g></svg>
      <span class="contact-text">urwebsitename.com</span>
    </li>
  </ul>

  <p class="brand-name">Brightkeel Logistics</p>
</section>

<section class="card card-back">
  <p class="brand-name">Brightkeel Logistics</p>
</section>

</body>
</html>
```